Design me a high response beautiful facebook ad

I need some really nice creative to support facebook advertising for a scheduling and time tracking tool called plenvo

Copy could be one of the following

"Change your life with beautifully simple rostering"

"Spreadsheets stink! There's a better way. Discovery How"

Font/text cannot be more than 20% of the area of the image.

Happy to use 'real people' and 'product shots' (take form website)

Please use the home page as inspiration.

i would like the brand (and sub brand to be prominent)

i dont have access to the raw files so please borrow from the website

1,200 x 628 pixels

Target Market(s)

Small business owners

Industry/Entity Type

Advertising

Font styles to use
Sans Serif

Colors
0355a3
3176b5
33a6d7
33b8a4

Requirements
Must have
• Logo
• Roughly consistent with colours at plenvo.com
Nice to have
• Product shot and /or real people
Should not have
• more than 20% of the area with text

```html
<!DOCTYPE html>
<html lang="en">
<head>
<meta charset="utf-8">
<title>plenvo – Change your life</title>
<link href="https://fonts.googleapis.com/css2?family=Open+Sans:ital,wght@0,400;0,600;0,700;0,800;1,700&display=swap" rel="stylesheet">
<style>
  :root {
    --frame: #2a2a2c;
    --accent: #1aa6f0;
    --accent-deep: #0355a3;
    --accent-mid: #3176b5;
    --ink: #333638;
    --brand-ink: #2f3133;
    --photo-light: #eef1f4;
    --shirt-light: #d7e0ec;
    --shirt-mid: #b9c8dc;
    --skin: #e6cdbf;
    --bar: #4a7fb8;
    --muted: #7c8791;
    --slice-red: #f25f5f;
    --slice-teal: #46c1a0;
    --slice-orange: #f6a45a;
    --slice-blue: #5b8fe0;
  }
  * { margin: 0; padding: 0; box-sizing: border-box; }
  html, body { width: 1200px; height: 628px; overflow: hidden; background: var(--frame); }
  .ad {
    position: relative; width: 1200px; height: 628px;
    background: var(--frame); overflow: hidden;
    font-family: "Open Sans", Arial, sans-serif;
  }
  .corner { position: absolute; z-index: 2; }
  .corner--top { top: 0; right: 0; }
  .corner--bottom { bottom: 0; left: 0; }
  .stage {
    position: absolute; left: 18px; top: 16px; width: 1164px; height: 596px;
    background: linear-gradient(100deg, var(--photo-light) 0%, #f7f8fa 55%, #eef1f4 100%);
    overflow: hidden;
  }
  .photo {
    position: absolute; left: 0; top: 0; width: 720px; height: 596px;
    background:
      radial-gradient(ellipse 190px 150px at 330px 60px, var(--skin) 0%, rgba(230,205,191,0) 100%),
      radial-gradient(ellipse 380px 330px at 290px 390px, var(--shirt-mid) 0%, var(--shirt-light) 55%, rgba(215,224,236,0) 100%),
      linear-gradient(90deg, #e3e9f0 0%, rgba(238,241,244,0) 100%);
  }
  .headline {
    position: absolute; right: 38px; top: 60px;
    font-size: 78px; font-weight: 700; font-style: italic;
    color: var(--accent); letter-spacing: -1px; line-height: 1;
  }
  .subline {
    position: absolute; right: 40px; top: 148px;
    font-size: 33px; font-weight: 400; color: var(--ink); line-height: 1;
  }
  .brand {
    position: absolute; left: 16px; top: 462px;
    font-size: 104px; font-weight: 800; color: var(--brand-ink);
    letter-spacing: -3px; line-height: 1;
  }
  .screen {
    position: absolute; left: 690px; top: 322px; width: 474px; height: 274px;
    background: #ffffff; border-radius: 14px 0 0 0;
    box-shadow: 0 6px 24px rgba(0,0,0,0.18);
    overflow: hidden;
  }
  .screen__tabs {
    display: flex; justify-content: space-around; align-items: center;
    height: 48px; background: var(--bar); color: #ffffff;
    font-size: 15px; font-weight: 600; letter-spacing: 0.5px;
  }
  .screen__meta {
    display: flex; justify-content: space-between; padding: 10px 28px 0 18px;
    font-size: 11px; color: var(--ink);
  }
  .screen__meta .label { font-weight: 600; text-transform: uppercase; }
  .screen__body { display: flex; align-items: center; padding: 4px 18px 0 40px; gap: 40px; }
  .legend { list-style: none; font-size: 13px; color: var(--ink); }
  .legend li { display: flex; align-items: center; gap: 10px; margin: 5px 0; }
  .legend .dot { width: 12px; height: 12px; border-radius: 3px; }
  .totals {
    position: absolute; bottom: 0; left: 0; right: 0; height: 50px;
    display: flex; border-top: 1px solid #e3e7eb;
  }
  .totals .cell { flex: 1; text-align: center; padding-top: 4px; border-left: 1px solid #e3e7eb; }
  .totals .cell:first-child { border-left: none; }
  .totals .period { font-size: 11px; color: var(--muted); text-transform: uppercase; }
  .totals .value { font-size: 19px; color: var(--ink); line-height: 1.3; }
</style>
</head>
<body>
<div class="ad">
  <svg class="corner corner--top" width="140" height="60" viewBox="0 0 140 60" aria-hidden="true">
    <polygon points="40,0 140,0 140,40" fill="var(--accent)"/>
  </svg>
  <svg class="corner corner--bottom" width="140" height="60" viewBox="0 0 140 60" aria-hidden="true">
    <polygon points="0,20 0,60 100,60" fill="var(--accent)"/>
  </svg>

  <div class="stage">
    <div class="photo" role="img" aria-label="Smiling businesswoman in a light blue shirt checking her schedule on a smartphone"></div>

    <h1 class="headline">Change your life</h1>
    <p class="subline">with beautifully simple rostering</p>

    <div class="screen">
      <div class="screen__tabs">
        <span class="tab">SUMMARY</span>
        <span class="tab">LIST</span>
      </div>
      <div class="screen__meta">
        <span class="label">Hours worked per position</span>
        <span>Jun 1 - Jun 30</span>
      </div>
      <div class="screen__body">
        <svg width="124" height="124" viewBox="-75 -75 150 150" aria-label="Hours by position chart">
          <g fill="none" stroke-width="44" transform="rotate(-90)">
            <circle r="50" stroke="var(--slice-red)" stroke-dasharray="188.5 314.2"/>
            <circle r="50" stroke="var(--slice-teal)" stroke-dasharray="78.5 314.2" stroke-dashoffset="-188.5"/>
            <circle r="50" stroke="var(--slice-orange)" stroke-dasharray="47.1 314.2" stroke-dashoffset="-267"/>
            <circle r="50" stroke="var(--slice-blue)" stroke-dasharray="31.4 314.2" stroke-dashoffset="-282.8"/>
          </g>
        </svg>
        <ul class="legend">
          <li><span class="dot" style="background:var(--slice-red)"></span>60% - Waiter</li>
          <li><span class="dot" style="background:var(--slice-teal)"></span>25% - Bartender</li>
          <li><span class="dot" style="background:var(--slice-orange)"></span>15% - Chef</li>
          <li><span class="dot" style="background:var(--slice-blue)"></span>10% - Other</li>
        </ul>
      </div>
      <div class="totals">
        <div class="cell"><div class="period">Week</div><div class="value">35 h 45 m</div></div>
        <div class="cell"><div class="period">Month</div><div class="value">123 h 20</div></div>
      </div>
    </div>

    <div class="brand">plenvo</div>
  </div>
</div>
</body>
</html>
```